Classic Car Web Banner Set Design

We need a set of banner ads designed for a manufacturing and retail company that sells weatherstripping for classic American vehicles (muscle cars, antique cars, classic cars). The banner ad must include our logo. There should be at least one car in the graphic, whole or partial. Our primary colors are Red and Black. Either a representation of auto weatherstripping or the words "Quality Weatherstripping" should be in the design.

Company name is "Harlow Gasket Works"

Sizes Needed: 300x250, 300x100, 728x90, 160x600, 120x90, 728x90, 234x60, 320x100, 750x100, 250x250

Target Market(s)

Consumer Audience, Classic Car Market

Industry/Entity Type

Retail

Font styles to use
Sans Serif

Colors
ec1f27

Requirements
Must have
• Red and Black primary colors. Company logo. Graphically show weatherstripping and/or automotive icons. If a vehicle is used, it must be an American vehicle.
Nice to have
• PSD files for selected entry.
Should not have
• no people

```html
<!DOCTYPE html>
<html lang="en">
<head>
<meta charset="utf-8">
<title>Harlow Gasket Works — Quality Weatherstripping Banner</title>
<link rel="stylesheet" href="https://fonts.googleapis.com/css2?family=Open+Sans:wght@600;700&display=swap">
<style>
  :root {
    --brand-red: #e0141c;
    --bg-top: #6c6c6c;
    --bg-mid: #9b9b9b;
    --bg-bottom: #8a8a8a;
    --car-blue: #2b3470;
    --car-blue-soft: rgba(43, 52, 112, 0);
    --text-light: #ffffff;
  }
  * { margin: 0; padding: 0; box-sizing: border-box; }
  html, body {
    width: 1200px;
    height: 148px;
    overflow: hidden;
  }
  .banner {
    position: relative;
    width: 1200px;
    height: 148px;
    overflow: hidden;
    background: linear-gradient(180deg, var(--bg-top) 0%, var(--bg-mid) 55%, var(--bg-bottom) 100%);
    font-family: "Open Sans", Arial, sans-serif;
  }
  .vehicle-photo {
    position: absolute;
    right: 0;
    top: 0;
    width: 450px;
    height: 148px;
    background: linear-gradient(90deg, var(--car-blue-soft) 0%, var(--car-blue) 35%, var(--car-blue) 100%);
  }
  .headline-band {
    position: absolute;
    left: 0;
    top: 20px;
    width: 605px;
    height: 69px;
    background: var(--brand-red);
    display: flex;
    align-items: center;
    padding-left: 74px;
  }
  .headline {
    color: var(--text-light);
    font-weight: 700;
    font-size: 40px;
    letter-spacing: -0.3px;
    white-space: nowrap;
  }
  .cta {
    position: absolute;
    left: 440px;
    top: 86px;
    width: 279px;
    height: 44px;
    background: var(--brand-red);
    color: var(--text-light);
    font-weight: 600;
    font-size: 21px;
    display: flex;
    align-items: center;
    justify-content: center;
    text-decoration: none;
    white-space: nowrap;
  }
</style>
</head>
<body>
  <div class="banner">
    <div class="vehicle-photo" role="img" aria-label="Photo of a dark blue classic American muscle car with white hood stripes, seen from the front three-quarter angle"></div>
    <div class="headline-band">
      <h1 class="headline">Quality Weatherstripping</h1>
    </div>
    <a class="cta" href="#">Click to learn more</a>
  </div>
</body>
</html>
```